Business cards for a tribute and obituary website

Our website is called Tribute Lantern.

It is a special place online for people to remember their loved ones who have passed away, through obituaries and tributes. Friends and family can also convey their condolences on the deceased's memorial page. Celebrating the life of the deceased and remembering their legacy is very important to us – death should not be just about grieving.

We would like the card to look tasteful and modern. The design should ideally not have colours that are too bright. The logo and website URL, www.tributelantern.example should be visible on the front of the card, with our slogan "Celebrating a life passed" on the back.

The design should communicate our purpose – remembering loved ones who have passed – and also a lighter tone of celebrating life. It should not look like a funeral director's card!

Our logo has been attached. Looking forward to some beautiful designs! Get creative :)
Updates

Project Deadline Extended
Reason: Thank you all for your designs. The rest of my team and I have not reached a decision on which design to select and I am collecting feedback from them. I will provide feedback for any changes that need to be made soon. It would be great if we could see more original designs and in more colours! We will definitely select a design by this deadline.

Industry/Entity Type

Business

Contact Information for Business Card

Wendy Lumb
Project Manager
614772390
wendylumb@tributelantern.example

Font styles to use
Serif
Sans Serif

Requirements
Must have
• Logo and website address (www.tributelantern.example) on the front.
Nice to have
• Hi designers! It would be nice to see alternative colours – feel free to try out colours that are tasteful and subtle. The colour of the business card does not have to be the same as the logo.
• We would also like to see the logo used in different ways, perhaps a glossy or embossed finish. The card should look stylish.

```html
<!DOCTYPE html>
<html lang="en">
<head>
<meta charset="utf-8">
<title>Tribute Lantern – Business Card</title>
<link rel="stylesheet" href="https://fonts.googleapis.com/css2?family=Bitter:wght@700&family=Exo+2:wght@400;500&display=swap">
<style>
  :root {
    --navy: #0b2d4f;
    --slate: #8b8d90;
    --stripe: #ffffff;
    --ink-light: #ffffff;
    --page: #e6e7e9;
    --sans: "Exo 2", Arial, sans-serif;
    --serif: "Bitter", Georgia, serif;
  }
  * { box-sizing: border-box; margin: 0; padding: 0; }
  html, body { width: 1200px; height: 900px; overflow: hidden; }
  body {
    background: var(--page);
    display: flex;
    flex-direction: column;
    align-items: center;
    justify-content: center;
    gap: 34px;
  }
  .card {
    position: relative;
    width: 700px;
    height: 400px;
    border-radius: 44px;
    overflow: hidden;
    background: var(--navy);
    box-shadow: 0 6px 18px rgba(0,0,0,0.18);
  }
  .card-front .panels { position: absolute; inset: 0; }
  .contact-block {
    position: absolute;
    left: 46px;
    top: 36px;
    color: var(--ink-light);
    font-family: var(--sans);
  }
  .holder-name {
    font-size: 23px;
    font-weight: 500;
    letter-spacing: 1px;
    text-transform: uppercase;
  }
  .holder-title { font-size: 15px; margin-top: 2px; }
  .address { font-size: 14px; line-height: 1.45; margin-top: 34px; }
  .contact-list { list-style: none; margin-top: 26px; font-size: 13.5px; line-height: 1.75; }
  .contact-list li { display: flex; align-items: center; gap: 9px; }
  .contact-list svg { width: 13px; height: 13px; fill: none; stroke: var(--ink-light); stroke-width: 1.6; flex: none; }
  .brand {
    display: flex;
    align-items: center;
    gap: 14px;
    color: var(--ink-light);
    font-family: var(--serif);
    font-weight: 700;
  }
  .brand-dot { border-radius: 50%; background: var(--ink-light); flex: none; }
  .card-front .brand { position: absolute; left: 440px; top: 160px; font-size: 27px; line-height: 1.05; }
  .card-front .brand-dot { width: 34px; height: 34px; }
  .card-back {
    display: flex;
    flex-direction: column;
    align-items: center;
    justify-content: center;
    gap: 22px;
  }
  .card-back .brand { font-size: 50px; gap: 20px; }
  .card-back .brand-dot { width: 52px; height: 52px; }
  .slogan {
    color: var(--ink-light);
    font-family: var(--sans);
    font-size: 18px;
    letter-spacing: 2px;
    text-transform: uppercase;
  }
</style>
</head>
<body>

<section class="card card-front" aria-label="Business card front">
  <svg class="panels" viewBox="0 0 700 400" preserveAspectRatio="none" aria-hidden="true">
    <path d="M0 0 H378 C360 140 330 280 292 400 H0 Z" fill="var(--stripe)"/>
    <path d="M0 0 H362 C344 140 314 280 276 400 H0 Z" fill="var(--slate)"/>
  </svg>

  <div class="contact-block">
    <p class="holder-name">Wendy Lumb</p>
    <p class="holder-title">Project Manager</p>
    <p class="address">47 Willow Lane, Unit 5<br>Harbour Road ELM</p>
    <ul class="contact-list">
      <li><svg viewBox="0 0 16 16"><path d="M4 1.5 L6.5 4.5 L5 6.5 C6 8.5 7.5 10 9.5 11 L11.5 9.5 L14.5 12 L12.5 14.5 C7 14 2 9 1.5 3.5 Z"/></svg>614 772 390</li>
      <li><svg viewBox="0 0 16 16"><rect x="4" y="1.5" width="8" height="4"/><rect x="1.5" y="5.5" width="13" height="6"/><rect x="4" y="9.5" width="8" height="5"/></svg>614 772 390</li>
      <li><svg viewBox="0 0 16 16"><rect x="4" y="1" width="8" height="14" rx="1.5"/><line x1="7" y1="12.5" x2="9" y2="12.5"/></svg>614 772 390</li>
      <li><svg viewBox="0 0 16 16"><circle cx="8" cy="8" r="3"/><path d="M11 8 V9.5 C11 11.5 14.5 11.5 14.5 8 A6.5 6.5 0 1 0 11 13.8"/></svg>wendylumb@tributelantern.example</li>
      <li><svg viewBox="0 0 16 16"><circle cx="8" cy="8" r="6.5"/><ellipse cx="8" cy="8" rx="2.8" ry="6.5"/><line x1="1.5" y1="8" x2="14.5" y2="8"/></svg>www.tributelantern.example</li>
    </ul>
  </div>

  <div class="brand">
    <span class="brand-dot"></span>
    <span class="brand-name">Tribute<br>Lantern</span>
  </div>
</section>

<section class="card card-back" aria-label="Business card back">
  <div class="brand">
    <span class="brand-dot"></span>
    <span class="brand-name">Tribute Lantern</span>
  </div>
  <p class="slogan">Celebrating a life passed</p>
</section>

</body>
</html>
```